Fenwick Partners - Client Appreciation Party Invitation and Poster

We need a printable invitation, a version of the same invitation that can be emailed out, and also a Poster of the invitation for our annual client appreciation party.

The location is called: The Larkspur Loft. Here is a link to the location: https://www.thelarkspurloftvenue.com/

We like their font and their little logo that you see when you log onto this page. But we'd love to see creatively what you can come up with.

This party is for our clients who are interior designers and owners in the Hospitality industry. Here are the details which need to be included in the invitation:

Location: The Larkspur Loft - 482 W Tamsin Ave. Chicago IL 60618
Date/Time: Thursday August 23rd - 5:30-9:00pm
RSVP: Please RSVP to: gathering@fenwickpartners.com

Then our Sponsors Logos need to be included on the bottom: I have uploaded those logos here as well as our Logo and a copy of the invitation we did for last year's party so you can see sort of what we've done in the past.

For the poster - we typically do a version of the invitation (see uploaded example of last year's poster) with the sponsor logos and the overall theme of the invitation just a bit simplified by removing the date/time/location info. We need this in a printable format which can be blown up to a 24x30 poster size.

Requirements
Must have
• use 2 to 3 colors only.
• logos of sponsors can be of the same color.

```html
<!DOCTYPE html>
<html lang="en">
<head>
<meta charset="utf-8">
<title>Fenwick Partners – Weekend Warm Up</title>
<link href="https://fonts.googleapis.com/css2?family=Cinzel:wght@400&family=Montserrat:wght@400;500&family=Oswald:wght@600&display=swap" rel="stylesheet">
<style>
  :root {
    --royal: #1c3c9e;
    --navy: #1a2a86;
    --ink: #1d1d1d;
    --text: #2b2b2b;
    --leaf: #7fb54a;
    --leaf-light: #c9e3a6;
    --paper: #fbfbf8;
    --rule: #8a8a8a;
  }
  * { margin: 0; padding: 0; box-sizing: border-box; }
  html, body { width: 857px; height: 1200px; overflow: hidden; background: var(--paper); }
  .invitation {
    position: relative; width: 857px; height: 1200px; background: var(--paper);
    font-family: "Montserrat", Arial, sans-serif; color: var(--text);
  }
  .frame-outer {
    position: absolute; left: 64px; top: 57px; width: 735px; height: 1082px;
    border: 4px solid var(--navy);
  }
  .frame-inner {
    position: absolute; left: 74px; top: 67px; width: 715px; height: 1062px;
    border: 1px solid var(--navy);
  }
  .corner-ornament {
    position: absolute; width: 140px; height: 140px;
    background: radial-gradient(circle, rgba(40,70,190,0.35) 0%, rgba(40,70,190,0.15) 45%, rgba(251,251,248,0) 70%);
  }
  .corner-ornament--top { left: 680px; top: 28px; }
  .corner-ornament--bottom { left: 32px; top: 1000px; }

  .host {
    position: absolute; top: 99px; width: 100%; text-align: center;
    font-size: 16px; letter-spacing: 5px; color: var(--ink);
  }
  .title {
    position: absolute; width: 100%; text-align: center;
    font-family: "Cinzel", "Times New Roman", serif; font-weight: 400;
    line-height: 1; letter-spacing: 1px;
  }
  .title--weekend { top: 128px; font-size: 82px; color: var(--royal); }
  .title--warm { top: 196px; font-size: 82px; color: var(--ink); }

  .wreath {
    position: absolute; left: 176px; top: 282px; width: 504px; height: 536px; border-radius: 50%;
    background: radial-gradient(circle, rgba(251,251,248,0) 40%, var(--leaf-light) 48%, var(--leaf) 58%, rgba(127,181,74,0.3) 66%, rgba(251,251,248,0) 71%);
  }
  .venue-circle {
    position: absolute; left: 256px; top: 380px; width: 348px; height: 348px; border-radius: 50%;
    background: var(--paper); border: 2px solid var(--leaf);
    display: flex; align-items: center; justify-content: center;
  }
  .venue-name {
    font-family: "Cinzel", "Times New Roman", serif; font-weight: 400;
    font-size: 27px; letter-spacing: 2px; color: var(--ink); text-align: center;
  }

  .event-name {
    position: absolute; top: 832px; width: 100%; text-align: center;
    font-family: "Oswald", "Arial Narrow", sans-serif; font-weight: 600;
    font-size: 51px; letter-spacing: 0.5px; color: var(--royal); line-height: 64px;
  }
  .detail {
    position: absolute; width: 100%; text-align: center;
    font-size: 15px; line-height: 20px; color: var(--ink);
  }
  .detail .value { color: var(--royal); }
  .detail--date { top: 904px; }
  .detail--time { top: 930px; }
  .detail--location { top: 954px; }
  .detail--note { top: 976px; font-size: 9.5px; line-height: 11px; }
  .rsvp { position: absolute; top: 992px; width: 100%; text-align: center; font-size: 15px; line-height: 20px; color: var(--ink); }
  .divider {
    position: absolute; left: 152px; top: 1022px; width: 544px; height: 1px;
    background: linear-gradient(90deg, rgba(138,138,138,0), var(--rule) 15%, var(--rule) 85%, rgba(138,138,138,0));
  }
  .sponsors {
    position: absolute; left: 230px; top: 1039px; width: 400px;
    display: grid; grid-template-columns: 140px 88px 172px; row-gap: 12px;
  }
  .sponsor {
    display: flex; align-items: center; justify-content: center; gap: 6px;
    height: 30px; font-size: 14px; font-weight: 500; color: var(--ink); white-space: nowrap;
  }
  .sponsor .mark { width: 10px; height: 10px; background: var(--ink); }
  .sponsor .mark--round { border-radius: 50%; }
</style>
</head>
<body>
<main class="invitation">
  <div class="frame-outer"></div>
  <div class="frame-inner"></div>
  <div class="corner-ornament corner-ornament--top" role="img" aria-label="Blue scrollwork corner ornament"></div>
  <div class="corner-ornament corner-ornament--bottom" role="img" aria-label="Blue scrollwork corner ornament"></div>

  <p class="host">FENWICK PARTNERS</p>
  <h1 class="title title--weekend">WEEKEND</h1>
  <h2 class="title title--warm">WARM UP</h2>

  <div class="wreath" role="img" aria-label="Watercolour wreath of green leaves and sprigs around the venue name"></div>
  <div class="venue-circle">
    <p class="venue-name">THE LARKSPUR LOFT</p>
  </div>

  <h3 class="event-name">CLIENT APPRECIATION EVENT</h3>
  <p class="detail detail--date">Date: <span class="value">August 23, 2018</span></p>
  <p class="detail detail--time">Time: <span class="value">5:30-9:00pm</span></p>
  <p class="detail detail--location">Location: <span class="value">The Larkspur Loft 482 W Tamsin Ave Chicago IL</span></p>
  <p class="detail detail--note">(located above Copper Finch)</p>
  <p class="rsvp">RSVP to gathering@fenwickpartners.com</p>
  <div class="divider"></div>

  <div class="sponsors">
    <div class="sponsor"><span class="mark"></span>Brightwell</div>
    <div class="sponsor">Orla</div>
    <div class="sponsor">Harlow Hospitality</div>
    <div class="sponsor"><span class="mark"></span>Kestrel</div>
    <div class="sponsor"><span class="mark mark--round"></span>Vantra</div>
    <div class="sponsor">Meridian</div>
  </div>
</main>
</body>
</html>
```